Qorvane Management LLC Business Card

The sample logo was attached for the business Card Design for Traffic Control Company named Qorvane Management LLC. Card design needs to have the company logo and colors match the logo color. It will be nice to show some images of Traffic control signs or cones, even roads closer that math the company services

Target Market(s)

Temporary traffic control. Road closer.

Industry/Entity Type

Construction

Contact Information for Business Card

basic information, name, job title, address, email phone, website

Font styles to use
Serif
Sans Serif

Colors
F0912C
F2A743
F7CA91
FBE8D2
FDF5EE
EE7325
F08F49
F5BC92
FAE3D3
FDF4ED

```html
<!DOCTYPE html>
<html lang="en">
<head>
<meta charset="utf-8">
<title>Qorvane Management LLC – Business Card</title>
<link rel="stylesheet" href="https://fonts.googleapis.com/css2?family=Montserrat:wght@300;400;500;600;700;800&display=swap">
<style>
  :root {
    --orange: #ef7230;
    --hazard-yellow: #fbd21a;
    --ink: #000000;
    --paper: #ffffff;
    --label-grey: #7b7b7b;
    --card-radius: 31px;
  }
  * { box-sizing: border-box; margin: 0; padding: 0; }
  html, body {
    width: 1200px; height: 1200px; overflow: hidden;
    background: var(--paper);
    font-family: "Montserrat", sans-serif;
  }
  .stage { position: relative; width: 1200px; height: 1200px; }

  .side-label {
    position: absolute; top: 198px; width: 200px;
    text-align: center; font-size: 22px; font-weight: 600;
    color: var(--label-grey); letter-spacing: 0.5px;
  }
  .side-label--front { left: 246px; }
  .side-label--back { left: 755px; }

  .card {
    position: absolute; top: 281px; width: 410px; height: 671px;
    border-radius: var(--card-radius); overflow: hidden;
    box-shadow: 0 6px 22px rgba(0,0,0,0.22);
  }
  .card--front { left: 149px; background: var(--ink); }
  .card--back { left: 656px; background: var(--orange); }

  .wordmark { text-align: center; line-height: 1; }
  .wordmark__name { display: block; font-size: 66px; font-weight: 700; letter-spacing: -1px; }
  .wordmark__suffix { display: block; font-size: 27px; font-weight: 400; letter-spacing: 3px; margin-top: 12px; }

  /* Front */
  .front-header {
    position: absolute; left: 0; top: 0; width: 100%; height: 217px;
    background: var(--paper);
  }
  .front-header .wordmark { padding-top: 48px; }
  .front-header .wordmark__name { color: var(--orange); }
  .front-header .wordmark__suffix { color: var(--ink); }

  .accent-stripe {
    position: absolute; left: 0; top: 217px; width: 100%; height: 19px;
    background: var(--orange);
  }
  .accent-stripe svg { position: absolute; left: 22px; top: 0; }

  .person { position: absolute; left: 46px; top: 284px; color: var(--paper); }
  .person__name { font-size: 31px; font-weight: 800; line-height: 1.15; }
  .person__title { font-size: 30px; font-weight: 300; line-height: 1.2; margin-top: 2px; }

  .contact-list { list-style: none; position: absolute; left: 48px; top: 0; width: 340px; }
  .contact-item {
    position: absolute; left: 0; display: flex; align-items: center; gap: 18px;
    color: var(--paper); font-size: 20px; font-weight: 400; white-space: nowrap;
  }
  .contact-item svg { flex: none; }
  .contact-item--address { top: 402px; }
  .contact-item--phone { top: 481px; }
  .contact-item--email { top: 554px; }

  /* Back */
  .hazard-band {
    position: absolute; left: 0; top: 0; width: 100%; height: 94px;
    background: var(--hazard-yellow);
  }
  .card--back .wordmark { position: absolute; left: 0; top: 164px; width: 100%; color: var(--paper); }
  .card--back .wordmark__name { font-size: 62px; }
  .card--back .wordmark__suffix { font-size: 25px; margin-top: 12px; }

  .cone-visual {
    position: absolute; left: 96px; top: 299px; width: 218px; height: 244px;
    background: radial-gradient(ellipse at 50% 55%, #f5bc92 0%, #e8692a 45%, var(--orange) 75%);
    border-radius: 12px;
  }
  .website {
    position: absolute; left: 0; top: 581px; width: 100%;
    text-align: center; color: var(--paper); font-size: 20px; font-weight: 700;
  }
</style>
</head>
<body>
<main class="stage">
  <div class="side-label side-label--front">FRONT</div>
  <div class="side-label side-label--back">BACK</div>

  <section class="card card--front" aria-label="Business card front">
    <header class="front-header">
      <div class="wordmark">
        <span class="wordmark__name">Qorvane</span>
        <span class="wordmark__suffix">MANAGEMENT LLC</span>
      </div>
    </header>
    <div class="accent-stripe">
      <svg width="34" height="19" viewBox="0 0 34 19" aria-hidden="true">
        <g stroke="#000" stroke-width="3">
          <line x1="4" y1="19" x2="12" y2="4"/>
          <line x1="12" y1="19" x2="20" y2="4"/>
          <line x1="20" y1="19" x2="28" y2="4"/>
        </g>
      </svg>
    </div>

    <div class="person">
      <div class="person__name">Mara Ellison</div>
      <div class="person__title">CEO</div>
    </div>

    <ul class="contact-list">
      <li class="contact-item contact-item--address">
        <svg width="36" height="36" viewBox="0 0 36 36" aria-hidden="true">
          <circle cx="18" cy="18" r="16.5" fill="none" stroke="var(--orange)" stroke-width="2"/>
          <path d="M18 27c-4-5-6-8-6-11a6 6 0 0 1 12 0c0 3-2 6-6 11z" fill="none" stroke="var(--orange)" stroke-width="2"/>
          <circle cx="18" cy="16" r="2.2" fill="none" stroke="var(--orange)" stroke-width="1.8"/>
        </svg>
        <span>Name of your street</span>
      </li>
      <li class="contact-item contact-item--phone">
        <svg width="36" height="36" viewBox="0 0 36 36" aria-hidden="true">
          <circle cx="18" cy="18" r="16.5" fill="none" stroke="var(--orange)" stroke-width="2"/>
          <rect x="13" y="9" width="10" height="18" rx="2" fill="none" stroke="var(--orange)" stroke-width="2"/>
          <line x1="16.5" y1="24" x2="19.5" y2="24" stroke="var(--orange)" stroke-width="1.8"/>
        </svg>
        <span>&nbsp;+1 555 0142 8679</span>
      </li>
      <li class="contact-item contact-item--email">
        <svg width="36" height="36" viewBox="0 0 36 36" aria-hidden="true">
          <circle cx="18" cy="18" r="16.5" fill="none" stroke="var(--orange)" stroke-width="2"/>
          <rect x="10" y="12" width="16" height="12" rx="1.5" fill="none" stroke="var(--orange)" stroke-width="2"/>
          <path d="M10.5 13l7.5 6 7.5-6" fill="none" stroke="var(--orange)" stroke-width="2"/>
        </svg>
        <span>mara@qorvane.com</span>
      </li>
    </ul>
  </section>

  <section class="card card--back" aria-label="Business card back">
    <div class="hazard-band" role="img" aria-label="Black and yellow chevron hazard band"></div>
    <div class="wordmark">
      <span class="wordmark__name">Qorvane</span>
      <span class="wordmark__suffix">MANAGEMENT LLC</span>
    </div>
    <div class="cone-visual" role="img" aria-label="Orange traffic cone with white reflective stripes"></div>
    <div class="website">www.qorvanemanagement.com</div>
  </section>
</main>
</body>
</html>
```